Want to go online this week, rush project, everything is there, just make it pretty

I need a pretty html5/css template for a already made site. Please do not rearrange anything unless you feel you can simplify the design. I have a raw site. Please play with the site by making an account with coupon code PLUMWALKERS for free signup. Log in, log out, download as many designs as you can, then log in and log out. See everything cause it's brand new and I need it neat and pretty over the next few days if not sooner. So, after all that, the site is http://StitchloomPatternHub.example
Updates

Is anyone working on something to submit? If you have something please submit asap as I will be closing this Sat night or Sunday morning

Industry/Entity Type

Online

Coding

Coded - Design and coding required

```html
<!DOCTYPE html>
<html lang="en">
<head>
<meta charset="utf-8">
<title>Stitchloom – Machine Embroidery Designs</title>
<link rel="stylesheet" href="https://fonts.googleapis.com/css2?family=Open+Sans:wght@400;600;700&family=PT+Sans+Narrow:wght@400;700&family=Playfair+Display:ital,wght@1,400&display=swap">
<style>
:root{
  --pink:#d2186e;
  --pink-dark:#a8105a;
  --plum:#7a0f47;
  --plum-dark:#5c0a35;
  --green:#2f7d2a;
  --navy:#1d3b6b;
  --ink:#333;
  --muted:#888;
  --line:#ddd;
  --grey-bg:#e9e9e9;
  --white:#fff;
}
*{box-sizing:border-box;margin:0;padding:0}
html,body{width:1200px;height:3934px;overflow:hidden}
body{background:var(--white);font-family:"Open Sans",Arial,sans-serif;color:var(--ink);font-size:12px;position:relative}
a{color:inherit;text-decoration:none}

/* Header */
.site-header{position:absolute;top:0;left:0;width:1200px;height:177px}
.brand{position:absolute;left:138px;top:40px;display:flex;align-items:center;gap:14px}
.brand-dot{width:34px;height:34px;border-radius:50%;background:var(--pink)}
.brand-name{font-family:"PT Sans Narrow",sans-serif;font-weight:700;font-size:48px;color:var(--pink)}
.top-nav{position:absolute;right:270px;top:11px;font-size:11px;font-weight:600;color:#222;white-space:nowrap}
.top-nav a{margin:0 1px}
.btn-signup{position:absolute;left:944px;top:4px;width:138px;height:30px;background:var(--navy);color:#fff;font-size:12px;font-weight:600;display:flex;align-items:center;justify-content:center;gap:8px;border-radius:2px}
.stat{position:absolute;top:70px;text-align:left}
.stat-num{font-family:"PT Sans Narrow",sans-serif;font-size:58px;color:#f07aa9;line-height:1}
.stat-label{font-size:10px;color:var(--muted);margin-top:4px}
.stat-designs{left:688px}
.stat-sets{left:888px}

/* Hero */
.hero{position:absolute;top:177px;left:0;width:1200px;height:413px;background:linear-gradient(90deg,#8a6a2e 0%,#c99a3a 18%,#e8d7a8 40%,#f4efe2 50%,#c9e0e8 62%,#6fb6c9 80%,#5b89b8 100%)}
.hero-art{position:absolute;inset:0}
.hero-copy{position:absolute;left:0;right:0;top:148px;text-align:center}
.hero-title{font-family:"PT Sans Narrow",sans-serif;font-weight:700;font-size:50px;color:#2b2b2b;line-height:1.05}
.hero-sub{font-size:15px;color:#555;margin-top:12px}
.btn-register{display:inline-flex;align-items:center;gap:14px;margin-top:22px;height:58px;padding:0 28px;background:var(--pink);color:#fff;font-weight:700;font-size:14px;border-radius:2px}

/* DVD band */
.dvd-band{position:absolute;top:590px;left:0;width:1200px;height:255px;background:var(--white)}
.dvd-title{position:absolute;left:155px;top:92px;font-family:"PT Sans Narrow",sans-serif;font-weight:700;font-size:44px;color:#222;white-space:nowrap}
.dvd-soon{position:absolute;left:425px;top:146px;font-family:"Playfair Display",serif;font-style:italic;font-size:15px;color:var(--pink)}
.dvd-art{position:absolute;left:575px;top:70px;width:110px;height:110px;background:linear-gradient(135deg,#f2f2f2,#bdbdbd);border-radius:4px}
.btn-preorder{position:absolute;left:800px;top:93px;width:228px;height:58px;background:var(--green);color:#fff;font-weight:700;font-size:15px;display:flex;align-items:center;justify-content:center;gap:16px;border-radius:2px}

/* Designs grid */
.catalog{position:absolute;top:845px;left:0;width:1200px;height:1300px;background:var(--grey-bg)}
.design-grid{position:absolute;left:150px;top:28px;width:967px;display:grid;grid-template-columns:repeat(3,315px);column-gap:11px;row-gap:12px}
.design-card{background:var(--white);height:342px;padding:12px;box-shadow:0 1px 3px rgba(0,0,0,.12)}
.design-art{height:176px;border-radius:2px}
.art-feather{background:radial-gradient(ellipse at 50% 50%,#b7b4e2 0%,#e9e8f6 55%,#fff 80%)}
.art-dog{background:radial-gradient(ellipse at 50% 50%,#c78fc5 0%,#efdcee 55%,#fff 80%)}
.art-owl{background:radial-gradient(ellipse at 50% 50%,#5a5fb0 0%,#d9daf0 55%,#fff 80%)}
.design-title{font-family:"PT Sans Narrow",sans-serif;font-weight:700;font-size:20px;margin-top:12px;color:#222}
.design-cats{font-size:8px;color:var(--muted);margin-top:2px}
.design-meta{display:flex;justify-content:space-between;margin-top:10px}
.design-count{font-size:11px;font-weight:700;line-height:1.3}
.format-box{width:130px}
.format-label{font-size:7px;color:var(--muted);margin-bottom:3px}
.format-grid{display:grid;grid-template-columns:repeat(5,1fr);gap:2px}
.format-grid span{background:#e9b3cf;color:var(--plum);font-size:7px;text-align:center;height:11px;line-height:11px}
.design-foot{display:flex;justify-content:space-between;align-items:flex-end;margin-top:10px}
.btn-view{display:inline-flex;align-items:center;gap:8px;height:28px;padding:0 14px;background:var(--pink);color:#fff;font-size:11px;font-weight:700;border-radius:2px}
.release{text-align:left;width:130px;font-size:8px;color:var(--muted)}
.release b{display:block;font-size:11px;color:#222}
.pager{position:absolute;top:1180px;left:150px;width:967px;display:flex;justify-content:space-between;font-size:13px;color:#555}
.pager-note{position:absolute;top:1265px;left:150px;font-size:9px;color:#999;line-height:1.5}

/* New designs strip */
.new-designs{position:absolute;top:2183px;left:0;width:1200px;height:237px;background:linear-gradient(180deg,var(--plum) 0%,var(--plum-dark) 100%)}
.section-title{font-family:"Playfair Display",serif;font-style:italic;font-size:34px;text-align:center;display:flex;align-items:center;justify-content:center;gap:18px}
.new-designs .section-title{color:#fff;padding-top:30px}
.rule{width:70px;height:1px;background:currentColor;opacity:.7}
.thumb-strip{position:absolute;left:0;top:100px;width:1200px;height:132px;display:flex;gap:4px;background:var(--white);padding:2px 0}
.thumb{flex:1;height:128px}

/* Categories */
.categories{position:absolute;top:2440px;left:0;width:1200px;height:960px}
.categories .section-title{color:var(--pink);padding-top:40px}
.cat-group{position:absolute;top:130px}
.cat-group.animals{left:150px}
.cat-group.tags{left:670px}
.cat-head{font-weight:700;font-size:13px;color:#222;margin-bottom:8px}
.cat-cols{display:flex;gap:6px}
.cat-cols ul{list-style:none;width:130px}
.cat-cols li{font-size:10.5px;line-height:19px;color:#444}

/* Footer */
.site-footer{position:absolute;top:3440px;left:0;width:1200px;height:494px;border-top:1px solid var(--line)}
.foot-links{position:absolute;top:60px;list-style:none}
.foot-links li{font-size:13px;line-height:22px;color:#333}
.foot-links.site{left:228px}
.foot-links.social{left:405px}
.foot-brand{position:absolute;left:830px;top:85px;display:flex;align-items:center;gap:12px}
.foot-brand .brand-name{font-size:40px}
.foot-brand .brand-dot{width:28px;height:28px}
.foot-bar{position:absolute;top:400px;left:150px;width:967px;border-top:1px solid var(--line);padding-top:22px;display:flex;justify-content:flex-end;align-items:center;gap:8px;font-size:12px;color:#555}
.social-sq{width:22px;height:22px;border-radius:3px}
</style>
</head>
<body>

<header class="site-header">
  <a class="brand" href="#"><span class="brand-dot"></span><span class="brand-name">Stitchloom</span></a>
  <nav class="top-nav"><a href="#">Home</a> | <a href="#">Register</a> | <a href="#">Account</a> | <a href="#">Contact</a> | <a href="#">Search</a> | <a href="#">Bookmark This Page</a></nav>
  <a class="btn-signup" href="#">Sign up
    <svg width="12" height="12" viewBox="0 0 12 12"><path d="M4 2l4 4-4 4" stroke="#fff" stroke-width="2" fill="none"/></svg>
  </a>
  <div class="stat stat-designs"><div class="stat-num">27,936</div><div class="stat-label">unique designs online</div></div>
  <div class="stat stat-sets"><div class="stat-num">1,982</div><div class="stat-label">design collections</div></div>
</header>

<section class="hero">
  <div class="hero-art" role="img" aria-label="Photograph of colourful embroidery thread skeins fanned around the edges"></div>
  <div class="hero-copy">
    <h1 class="hero-title">Thousands of machine ready<br>embroidery designs</h1>
    <p class="hero-sub">Lorem ipsum Consectetur Adipiscing Elit</p>
    <a class="btn-register" href="#">REGISTER NOW
      <svg width="18" height="18" viewBox="0 0 18 18"><rect x="1" y="3" width="12" height="12" fill="none" stroke="#fff" stroke-width="2"/><path d="M8 10l8-8" stroke="#fff" stroke-width="2"/></svg>
    </a>
  </div>
</section>

<section class="dvd-band">
  <h2 class="dvd-title">Get all designs on DVD</h2>
  <span class="dvd-soon">Coming soon!</span>
  <div class="dvd-art" role="img" aria-label="Illustration of a DVD case with disc"></div>
  <a class="btn-preorder" href="#">PRE-ORDER NOW
    <svg width="18" height="18" viewBox="0 0 18 18"><rect x="1" y="1" width="16" height="16" fill="none" stroke="#fff" stroke-width="2"/><path d="M5 9h8M9 5v8" stroke="#fff" stroke-width="2"/></svg>
  </a>
</section>

<section class="catalog">
  <div class="design-grid">
    <article class="design-card">
      <div class="design-art art-feather" role="img" aria-label="Embroidery design of a lavender feather"></div>
      <h3 class="design-title">Light As A Feather</h3>
      <p class="design-cats">Categories: Birds, Nature, Feathers, Objects</p>
      <div class="design-meta">
        <div class="design-count">10 Designs<br>All fit the 4x4 hoop</div>
        <div class="format-box"><div class="format-label">Available file formats</div><div class="format-grid"><span>ART</span><span>DST</span><span>EXP</span><span>HUS</span><span>JEF</span><span>PES</span><span>SEW</span><span>VIP</span><span>VP3</span><span>XXX</span></div></div>
      </div>
      <div class="design-foot"><a class="btn-view" href="#"><svg width="10" height="10" viewBox="0 0 10 10"><circle cx="5" cy="5" r="4" fill="#fff"/></svg>View Set</a><div class="release">Released date<b>October 08, 2013</b></div></div>
    </article>
    <article class="design-card">
      <div class="design-art art-dog" role="img" aria-label="Embroidery design of a girl walking a dog"></div>
      <h3 class="design-title">Walking the Dog</h3>
      <p class="design-cats">Categories: Pets, Dogs, People, Kids</p>
      <div class="design-meta">
        <div class="design-count">10 Designs<br>All fit the 4x4 hoop</div>
        <div class="format-box"><div class="format-label">Available file formats</div><div class="format-grid"><span>ART</span><span>DST</span><span>EXP</span><span>HUS</span><span>JEF</span><span>PES</span><span>SEW</span><span>VIP</span><span>VP3</span><span>XXX</span></div></div>
      </div>
      <div class="design-foot"><a class="btn-view" href="#"><svg width="10" height="10" viewBox="0 0 10 10"><circle cx="5" cy="5" r="4" fill="#fff"/></svg>View Set</a><div class="release">Released date<b>August 21, 2014</b></div></div>
    </article>
    <article class="design-card">
      <div class="design-art art-owl" role="img" aria-label="Embroidery design of an owl in a witch hat"></div>
      <h3 class="design-title">Whooo Am I</h3>
      <p class="design-cats">Categories: Birds, Owls, Halloween, Autumn</p>
      <div class="design-meta">
        <div class="design-count">10 Designs<br>All fit the 4x4 hoop</div>
        <div class="format-box"><div class="format-label">Available file formats</div><div class="format-grid"><span>ART</span><span>DST</span><span>EXP</span><span>HUS</span><span>JEF</span><span>PES</span><span>SEW</span><span>VIP</span><span>VP3</span><span>XXX</span></div></div>
      </div>
      <div class="design-foot"><a class="btn-view" href="#"><svg width="10" height="10" viewBox="0 0 10 10"><circle cx="5" cy="5" r="4" fill="#fff"/></svg>View Set</a><div class="release">Released date<b>September 22, 2014</b></div></div>
    </article>
    <article class="design-card">
      <div class="design-art art-feather" role="img" aria-label="Embroidery design of a lavender feather"></div>
      <h3 class="design-title">Light As A Feather</h3>
      <p class="design-cats">Categories: Birds, Nature, Feathers, Objects</p>
      <div class="design-meta">
        <div class="design-count">10 Designs<br>All fit the 4x4 hoop</div>
        <div class="format-box"><div class="format-label">Available file formats</div><div class="format-grid"><span>ART</span><span>DST</span><span>EXP</span><span>HUS</span><span>JEF</span><span>PES</span><span>SEW</span><span>VIP</span><span>VP3</span><span>XXX</span></div></div>
      </div>
      <div class="design-foot"><a class="btn-view" href="#"><svg width="10" height="10" viewBox="0 0 10 10"><circle cx="5" cy="5" r="4" fill="#fff"/></svg>View Set</a><div class="release">Released date<b>October 08, 2013</b></div></div>
    </article>
    <article class="design-card">
      <div class="design-art art-dog" role="img" aria-label="Embroidery design of a girl walking a dog"></div>
      <h3 class="design-title">Walking the Dog</h3>
      <p class="design-cats">Categories: Pets, Dogs, People, Kids</p>
      <div class="design-meta">
        <div class="design-count">10 Designs<br>All fit the 4x4 hoop</div>
        <div class="format-box"><div class="format-label">Available file formats</div><div class="format-grid"><span>ART</span><span>DST</span><span>EXP</span><span>HUS</span><span>JEF</span><span>PES</span><span>SEW</span><span>VIP</span><span>VP3</span><span>XXX</span></div></div>
      </div>
      <div class="design-foot"><a class="btn-view" href="#"><svg width="10" height="10" viewBox="0 0 10 10"><circle cx="5" cy="5" r="4" fill="#fff"/></svg>View Set</a><div class="release">Released date<b>August 21, 2014</b></div></div>
    </article>
    <article class="design-card">
      <div class="design-art art-owl" role="img" aria-label="Embroidery design of an owl in a witch hat"></div>
      <h3 class="design-title">Whooo Am I</h3>
      <p class="design-cats">Categories: Birds, Owls, Halloween, Autumn</p>
      <div class="design-meta">
        <div class="design-count">10 Designs<br>All fit the 4x4 hoop</div>
        <div class="format-box"><div class="format-label">Available file formats</div><div class="format-grid"><span>ART</span><span>DST</span><span>EXP</span><span>HUS</span><span>JEF</span><span>PES</span><span>SEW</span><span>VIP</span><span>VP3</span><span>XXX</span></div></div>
      </div>
      <div class="design-foot"><a class="btn-view" href="#"><svg width="10" height="10" viewBox="0 0 10 10"><circle cx="5" cy="5" r="4" fill="#fff"/></svg>View Set</a><div class="release">Released date<b>September 22, 2014</b></div></div>
    </article>
    <article class="design-card">
      <div class="design-art art-feather" role="img" aria-label="Embroidery design of a lavender feather"></div>
      <h3 class="design-title">Light As A Feather</h3>
      <p class="design-cats">Categories: Birds, Nature, Feathers, Objects</p>
      <div class="design-meta">
        <div class="design-count">10 Designs<br>All fit the 4x4 hoop</div>
        <div class="format-box"><div class="format-label">Available file formats</div><div class="format-grid"><span>ART</span><span>DST</span><span>EXP</span><span>HUS</span><span>JEF</span><span>PES</span><span>SEW</span><span>VIP</span><span>VP3</span><span>XXX</span></div></div>
      </div>
      <div class="design-foot"><a class="btn-view" href="#"><svg width="10" height="10" viewBox="0 0 10 10"><circle cx="5" cy="5" r="4" fill="#fff"/></svg>View Set</a><div class="release">Released date<b>October 08, 2013</b></div></div>
    </article>
    <article class="design-card">
      <div class="design-art art-dog" role="img" aria-label="Embroidery design of a girl walking a dog"></div>
      <h3 class="design-title">Walking the Dog</h3>
      <p class="design-cats">Categories: Pets, Dogs, People, Kids</p>
      <div class="design-meta">
        <div class="design-count">10 Designs<br>All fit the 4x4 hoop</div>
        <div class="format-box"><div class="format-label">Available file formats</div><div class="format-grid"><span>ART</span><span>DST</span><span>EXP</span><span>HUS</span><span>JEF</span><span>PES</span><span>SEW</span><span>VIP</span><span>VP3</span><span>XXX</span></div></div>
      </div>
      <div class="design-foot"><a class="btn-view" href="#"><svg width="10" height="10" viewBox="0 0 10 10"><circle cx="5" cy="5" r="4" fill="#fff"/></svg>View Set</a><div class="release">Released date<b>August 21, 2014</b></div></div>
    </article>
    <article class="design-card">
      <div class="design-art art-owl" role="img" aria-label="Embroidery design of an owl in a witch hat"></div>
      <h3 class="design-title">Whooo Am I</h3>
      <p class="design-cats">Categories: Birds, Owls, Halloween, Autumn</p>
      <div class="design-meta">
        <div class="design-count">10 Designs<br>All fit the 4x4 hoop</div>
        <div class="format-box"><div class="format-label">Available file formats</div><div class="format-grid"><span>ART</span><span>DST</span><span>EXP</span><span>HUS</span><span>JEF</span><span>PES</span><span>SEW</span><span>VIP</span><span>VP3</span><span>XXX</span></div></div>
      </div>
      <div class="design-foot"><a class="btn-view" href="#"><svg width="10" height="10" viewBox="0 0 10 10"><circle cx="5" cy="5" r="4" fill="#fff"/></svg>View Set</a><div class="release">Released date<b>September 22, 2014</b></div></div>
    </article>
  </div>
  <div class="pager"><span>Page 1 of 84</span><a href="#">Next Page &rarr;</a></div>
  <p class="pager-note">Please be advised that all designs are sized to fit the hoop listed and may vary slightly by machine brand.<br>Designs are delivered as zip files and can be downloaded again at any time from your account.</p>
</section>

<section class="new-designs">
  <h2 class="section-title"><span class="rule"></span>New designs<span class="rule"></span></h2>
  <div class="thumb-strip">
    <div class="thumb" role="img" aria-label="New design thumbnail" style="background:#b9c7e6"></div>
    <div class="thumb" role="img" aria-label="New design thumbnail" style="background:#d9a88a"></div>
    <div class="thumb" role="img" aria-label="New design thumbnail" style="background:#7b8fc9"></div>
    <div class="thumb" role="img" aria-label="New design thumbnail" style="background:#cfcfcf"></div>
    <div class="thumb" role="img" aria-label="New design thumbnail" style="background:#9a9a9a"></div>
    <div class="thumb" role="img" aria-label="New design thumbnail" style="background:#e0e0e0"></div>
    <div class="thumb" role="img" aria-label="New design thumbnail" style="background:#8a6b5a"></div>
    <div class="thumb" role="img" aria-label="New design thumbnail" style="background:#6d8f4e"></div>
    <div class="thumb" role="img" aria-label="New design thumbnail" style="background:#e7b4a5"></div>
    <div class="thumb" role="img" aria-label="New design thumbnail" style="background:#5d7ab0"></div>
  </div>
</section>

<section class="categories">
  <h2 class="section-title"><span class="rule"></span>Categories<span class="rule"></span></h2>
  <div class="cat-group animals">
    <div class="cat-head">Animals</div>
    <div class="cat-cols">
      <ul><li>Aardvark (3)</li><li>Alligator (12)</li><li>Alpaca (4)</li><li>Angelfish (6)</li><li>Ant (9)</li><li>Ape (5)</li><li>Badger (3)</li><li>Bat (14)</li><li>Bear (48)</li><li>Beaver (7)</li><li>Bee (22)</li><li>Beetle (8)</li><li>Bighorn Sheep (2)</li><li>Bird (96)</li><li>Bison (4)</li><li>Boar (3)</li><li>Bull (11)</li><li>Bunny (36)</li><li>Butterfly (64)</li><li>Camel (5)</li><li>Cardinal (9)</li><li>Cat (72)</li><li>Chick (18)</li><li>Chicken (15)</li></ul>
      <ul><li>Cow (21)</li><li>Crab (6)</li><li>Crane (4)</li><li>Crow (7)</li><li>Deer (19)</li><li>Dinosaur (16)</li><li>Dog (88)</li><li>Dolphin (10)</li><li>Donkey (5)</li><li>Dove (13)</li><li>Dragon (17)</li><li>Dragonfly (12)</li><li>Duck (24)</li><li>Eagle (14)</li><li>Elephant (20)</li><li>Elk (3)</li><li>Fish (31)</li><li>Flamingo (6)</li><li>Fox (15)</li><li>Frog (23)</li><li>Giraffe (11)</li><li>Goat (8)</li><li>Goose (7)</li><li>Gorilla (4)</li></ul>
      <ul><li>Hamster (5)</li><li>Hedgehog (6)</li><li>Hippo (9)</li><li>Horse (42)</li><li>Hummingbird (8)</li><li>Kangaroo (4)</li><li>Koala (6)</li><li>Ladybug (18)</li><li>Lamb (14)</li><li>Lion (16)</li><li>Lizard (7)</li><li>Monkey (25)</li><li>Moose (5)</li><li>Mouse (20)</li><li>Octopus (6)</li><li>Owl (39)</li><li>Panda (12)</li><li>Parrot (9)</li><li>Penguin (17)</li><li>Pig (22)</li><li>Raccoon (6)</li><li>Squirrel (11)</li><li>Tiger (10)</li><li>Turtle (19)</li></ul>
    </div>
  </div>
  <div class="cat-group tags">
    <div class="cat-head">Tags</div>
    <div class="cat-cols">
      <ul><li>Alphabet (28)</li><li>Angels (14)</li><li>Anniversary (6)</li><li>Applique (52)</li><li>Autumn (33)</li><li>Baby (47)</li><li>Baking (9)</li><li>Beach (15)</li><li>Birthday (21)</li><li>Borders (18)</li><li>Boys (26)</li><li>Camping (7)</li><li>Cars (12)</li><li>Celtic (10)</li><li>Children (44)</li><li>Christmas (71)</li><li>Circus (8)</li><li>Coffee (6)</li><li>Cowboy (11)</li><li>Crosses (9)</li><li>Cupcakes (13)</li><li>Dance (5)</li><li>Easter (24)</li><li>Fairies (16)</li></ul>
      <ul><li>Fall Leaves (12)</li><li>Farm (30)</li><li>Fishing (8)</li><li>Floral (85)</li><li>Food (19)</li><li>Football (7)</li><li>Friends (10)</li><li>Fruit (14)</li><li>Garden (27)</li><li>Girls (38)</li><li>Golf (5)</li><li>Graduation (6)</li><li>Halloween (34)</li><li>Hearts (29)</li><li>Holidays (40)</li><li>Home (17)</li><li>Hunting (4)</li><li>Kitchen (22)</li><li>Lace (15)</li><li>Monogram (20)</li><li>Music (9)</li><li>Nautical (11)</li><li>Ocean (16)</li><li>Paisley (7)</li></ul>
      <ul><li>Patriotic (13)</li><li>Quilting (25)</li><li>Rainbows (6)</li><li>Redwork (18)</li><li>Religious (12)</li><li>Retro (9)</li><li>Roses (21)</li><li>School (14)</li><li>Sewing (19)</li><li>Snowman (15)</li><li>Spring (28)</li><li>Stars (17)</li><li>Summer (24)</li><li>Sports (20)</li><li>Swirls (11)</li><li>Tea Time (8)</li><li>Thanksgiving (7)</li><li>Toys (13)</li><li>Trains (5)</li><li>Travel (6)</li><li>Valentine (19)</li><li>Vintage (23)</li><li>Wedding (10)</li><li>Winter (26)</li></ul>
    </div>
  </div>
</section>

<footer class="site-footer">
  <ul class="foot-links site"><li><a href="#">Home</a></li><li><a href="#">Register</a></li><li><a href="#">Account</a></li><li><a href="#">Contact</a></li><li><a href="#">Search</a></li><li><a href="#">Bookmark this page</a></li></ul>
  <ul class="foot-links social"><li><a href="#">Friendbook</a></li><li><a href="#">Chirper</a></li><li><a href="#">LinkUp</a></li><li><a href="#">Circles</a></li><li><a href="#">ViewTube</a></li></ul>
  <a class="brand foot-brand" href="#"><span class="brand-dot"></span><span class="brand-name">Stitchloom</span></a>
  <div class="foot-bar">
    <span>Get Social</span>
    <span class="social-sq" style="background:#3b5a98"></span>
    <span class="social-sq" style="background:#3aa7dc"></span>
    <span class="social-sq" style="background:#2a7bb5"></span>
    <span class="social-sq" style="background:#d04a38"></span>
    <span class="social-sq" style="background:#c3262a"></span>
  </div>
</footer>

</body>
</html>
```